Real Estate Seller Financing Postcard

I need a postcard that lays out these options contained in the notes that grabs attention, explains the two options easily and is eye-catching. The front needs to have the percentages on it and information about it and on the other side One side exact Text is:
"Monthly income without tenant headaches" in big letters. Also on front "Get
110%
add an "or"
160% of market value for your property. ". The percentages should be displayed and that is not to be a sentence of text. Other side text: I need bullets points for these "Formal protection as a lien holder against home
No commission or closing cost
Fast closings possible
Property taken as is so no repairs.

Add to the top of the back in "It’s simple. I am a new investor without down payment capital who still want to double our portfolio this year to grow our portfolio."
Here are the two options that are to be the largest part of the back
Option 1, you can receive 80% now cash and 30% over a short period of time including interest.

Option 2, where act like a bank allowing you to make 150% if you finance the whole property(ies). No gimmicks and surprises, just simple unconventional financing.

Include Logo Somewhere

Target Market(s)

Property Owners Wanting to Sell Their Property

Industry/Entity Type

Real Estate Investing

Requirements
Must have
• The options promiment and each side with its respective information. Must have logo somewhere
Nice to have
• The options in color other than black.
Should not have
• A picture of money on the front. Any other image is okay.

```html
<!DOCTYPE html>
<html lang="en">
<head>
<meta charset="UTF-8">
<title>Meridian Real Estate Group – Seller Financing Postcard</title>
<link href="https://fonts.googleapis.com/css2?family=Anton&family=Open+Sans:wght@400;600;700;800&display=swap" rel="stylesheet">
<style>
  :root {
    --blue: #1b3f95;
    --ink: #222326;
    --paper: #f5f5f6;
    --panel: #e3e3e4;
    --muted: #7d7f86;
    --stage: #7e7e7e;
    --white: #ffffff;
  }
  * { box-sizing: border-box; margin: 0; padding: 0; }
  html, body { width: 1200px; height: 900px; overflow: hidden; }
  body {
    background: var(--stage);
    font-family: "Open Sans", Arial, sans-serif;
    display: flex;
    align-items: center;
    justify-content: center;
    gap: 30px;
  }
  .postcard {
    position: relative;
    width: 560px;
    height: 374px;
    background: var(--paper);
    overflow: hidden;
    box-shadow: 0 6px 16px rgba(0,0,0,.25);
  }

  /* brand lockup */
  .brand { display: flex; align-items: center; gap: 10px; }
  .brand-mark { width: 40px; height: 40px; border: 2px solid var(--blue); border-radius: 50%; flex: none; }
  .brand-rule { width: 1px; height: 34px; background: var(--muted); flex: none; }
  .brand-name { color: var(--blue); font-weight: 600; line-height: 1; white-space: nowrap; }
  .brand-name .primary { display: block; font-size: 22px; letter-spacing: 1px; }
  .brand-name .secondary { display: block; font-size: 8px; letter-spacing: 1px; margin-top: 3px; }

  /* front */
  .front .brand { position: absolute; left: 26px; top: 26px; }
  .headline {
    position: absolute; left: 30px; top: 92px;
    font-family: "Anton", Impact, sans-serif;
    font-weight: 400;
    font-size: 39px; line-height: 1.05; letter-spacing: .3px;
    text-transform: uppercase;
  }
  .headline .accent { color: var(--blue); display: block; }
  .headline .dark { color: var(--ink); display: block; }
  .hero-image {
    position: absolute; right: 22px; top: 18px;
    width: 236px; height: 244px;
    background: radial-gradient(ellipse at 45% 40%, #d9c3a3 0%, #b7b89d 45%, #8f9a84 75%, var(--paper) 100%);
  }
  .offer-band {
    position: absolute; left: 0; right: 0; bottom: 0; height: 100px;
    background: var(--blue); color: var(--white);
    display: flex; align-items: center; justify-content: center; gap: 8px;
    padding: 0 18px;
    font-family: "Anton", Impact, sans-serif; text-transform: uppercase;
    border-top: 6px solid var(--paper);
  }
  .offer-small { font-size: 19px; }
  .offer-figure { font-size: 46px; line-height: 1; }
  .offer-or {
    width: 54px; height: 54px; border-radius: 50%;
    background: var(--white); color: var(--blue);
    display: flex; align-items: center; justify-content: center;
    font-size: 26px; flex: none;
  }
  .offer-note {
    font-family: "Open Sans", Arial, sans-serif; font-weight: 800;
    font-size: 11.5px; line-height: 1.2; white-space: nowrap;
  }

  /* back */
  .message { position: absolute; left: 0; top: 0; width: 336px; height: 100%; }
  .intro {
    background: var(--panel);
    padding: 20px 22px 12px 26px;
    font-size: 11px; line-height: 1.35; color: var(--ink);
    text-align: justify;
  }
  .benefits { list-style: none; padding: 10px 20px 0 30px; }
  .benefits li {
    display: flex; gap: 8px; align-items: flex-start;
    font-size: 11px; line-height: 1.3; color: var(--ink); margin-bottom: 3px;
  }
  .benefits svg { flex: none; margin-top: 2px; }
  .option-band {
    position: absolute; left: 0; bottom: 0; width: 100%; height: 176px;
    background: var(--blue); color: var(--white);
    padding: 14px 20px 0 28px;
    font-weight: 800; font-size: 12.5px; line-height: 1.3; text-align: justify;
  }
  .option-band p + p { margin-top: 8px; }
  .divider { position: absolute; left: 344px; top: 0; bottom: 0; width: 2px; background: var(--blue); }
  .address-side { position: absolute; left: 346px; top: 0; right: 0; bottom: 0; }
  .address-side .brand { position: absolute; left: 22px; top: 92px; gap: 7px; }
  .address-side .brand-mark { width: 26px; height: 26px; }
  .address-side .brand-rule { height: 22px; }
  .address-side .brand-name .primary { font-size: 14px; }
  .address-side .brand-name .secondary { font-size: 5.5px; }
  .stamp { position: absolute; right: 22px; top: 22px; width: 66px; height: 56px; border: 1.5px solid var(--muted); }
  .address-lines { position: absolute; left: 22px; right: 22px; top: 170px; }
  .address-lines span { display: block; height: 1px; background: var(--muted); margin-bottom: 34px; }
</style>
</head>
<body>

  <section class="postcard front" aria-label="Postcard front">
    <div class="brand">
      <span class="brand-mark"></span>
      <span class="brand-rule"></span>
      <span class="brand-name"><span class="primary">MERIDIAN</span><span class="secondary">REAL ESTATE GROUP</span></span>
    </div>
    <h1 class="headline">
      <span class="accent">Monthly Income</span>
      <span class="dark">Without Tenant</span>
      <span class="accent">Headaches</span>
    </h1>
    <div class="hero-image" role="img" aria-label="Photo of a money bag on a pile of bank notes"></div>
    <div class="offer-band">
      <span class="offer-small">Get</span>
      <span class="offer-figure">110%</span>
      <span class="offer-small">Add an</span>
      <span class="offer-or">OR</span>
      <span class="offer-figure">160%</span>
      <span class="offer-note">Of market value<br>for your property</span>
    </div>
  </section>

  <section class="postcard back" aria-label="Postcard back">
    <div class="message">
      <p class="intro">It’s simple. I am a new investor without down payment capital who still want to double our portfolio this year to grow our portfolio.</p>
      <ul class="benefits">
        <li><svg width="11" height="11" viewBox="0 0 11 11"><circle cx="5.5" cy="5.5" r="5.5" fill="#1b3f95"/><path d="M3 5.6l1.7 1.6L8 3.9" stroke="#fff" stroke-width="1.4" fill="none"/></svg>Formal protection as a lien holder against home</li>
        <li><svg width="11" height="11" viewBox="0 0 11 11"><circle cx="5.5" cy="5.5" r="5.5" fill="#1b3f95"/><path d="M3 5.6l1.7 1.6L8 3.9" stroke="#fff" stroke-width="1.4" fill="none"/></svg>No commission or closing cost</li>
        <li><svg width="11" height="11" viewBox="0 0 11 11"><circle cx="5.5" cy="5.5" r="5.5" fill="#1b3f95"/><path d="M3 5.6l1.7 1.6L8 3.9" stroke="#fff" stroke-width="1.4" fill="none"/></svg>Fast closings possible</li>
        <li><svg width="11" height="11" viewBox="0 0 11 11"><circle cx="5.5" cy="5.5" r="5.5" fill="#1b3f95"/><path d="M3 5.6l1.7 1.6L8 3.9" stroke="#fff" stroke-width="1.4" fill="none"/></svg>Property taken as is so no repairs.</li>
      </ul>
      <div class="option-band">
        <p class="option">Option 1, you can receive 80% now cash and 30% over a short period of time including interest.</p>
        <p class="option">Option 2, where act like a bank allowing you to make 150% if you finance the whole property(ies). No gimmicks and surprises, just simple unconventional financing.</p>
      </div>
    </div>
    <div class="divider"></div>
    <div class="address-side">
      <div class="stamp"></div>
      <div class="brand">
        <span class="brand-mark"></span>
        <span class="brand-rule"></span>
        <span class="brand-name"><span class="primary">MERIDIAN</span><span class="secondary">REAL ESTATE GROUP</span></span>
      </div>
      <div class="address-lines"><span></span><span></span><span></span></div>
    </div>
  </section>

</body>
</html>
```